Coffee bag product stickers

We currently have 4 blends of coffee (http://www.velmonbrew.com.au/ourcoffee,html) and would like to create a simple design that will be printed on clear/transparent product stickers to be placed on the front of the bags. The bags will be either black or brown so the design will need to work on both.
The design should have a consistent theme across the 4 blends with subtle differences in design or colour used to differentiate between them.
The labels we are looking at are rectangular clear poly synthetic labels, 102 x 76 mm
Information that should be incorporated in the designs is:
- our web site addresses ( www.velmonbrew.com.au )
- Name of the blend
- our logo (please see uploaded files)
Updates
Hi,
The original dimension of 100mm x 100mm have had to be altered to now be 102 mm x 76 mm. Designs do not need to fill this space completely as they will be printed on clear stickers allowing the colour of the bag to show through, however designs should also not be too small.
Many thanks.
FYI - The labels will be printed on clear label stock so the design does not need to fill the whole area and can use the colour of the bag (black - possibly brown on organic) to show through.
The idea is for it to be a sticker we place on the bag in order but for it not to look like a sticker if that make sense. It should almost be like a decal.
Thanks.
Reason: We have seen some excellent ideas and design approaches that never occurred to us while still managing to meet the brief and this is really pleasing. This has prompted us to extend the deadline to encourage more ideas for us to consider and allow us to extend our thinking even further.
Also, we felt completing the project directly after a weekend to be less than ideal.
Also, project is now a committed payment project.
Keep the ideas coming!!
Thanks,
Wallace
Colors
Designer to choose colors to be used in the design.

```html
<!DOCTYPE html>
<html lang="en">
<head>
<meta charset="utf-8">
<title>Velmon Brew – Fairtrade Organic Blend sticker</title>
<link href="https://fonts.googleapis.com/css2?family=Cinzel:wght@400;600;700&display=swap" rel="stylesheet">
<style>
  :root {
    --canvas: #000000;
    --label-base: #0b0b0b;
    --flourish-dark: #161616;
    --flourish-light: #2a2a2a;
    --gold-deep: #a86d2c;
    --gold-mid: #c8913f;
    --gold-shine: #f7e6c8;
    --blend-green: #3b7d2d;
    --type-white: #ffffff;
    --bean-dark: #3e2414;
    --bean-light: #9a6540;
    --guide: #3d3d3d;
    --guide-text: #4a4a4a;
  }
  html, body {
    margin: 0;
    padding: 0;
    width: 1200px;
    height: 1000px;
    overflow: hidden;
    background: var(--canvas);
  }
  .artboard { display: block; width: 1200px; height: 1000px; }
  .size-guide line { stroke: var(--guide); stroke-width: 1; }
  .size-guide path { fill: none; stroke: var(--guide); stroke-width: 1; }
  .size-label { fill: var(--guide-text); font: 400 13px Arial, Helvetica, sans-serif; }
  .label-base { fill: var(--label-base); }
  .flourish-field { fill: url(#flourishTone); }
  .gold-band { fill: url(#goldSheen); }
  .brand-name {
    fill: var(--type-white);
    font-family: "Cinzel", "Trajan Pro", serif;
    font-weight: 600;
    font-size: 54px;
  }
  .bean-photo { fill: url(#beanTone); }
  .blend-ribbon { fill: var(--blend-green); }
  .blend-name {
    fill: var(--type-white);
    font-family: "Cinzel", "Trajan Pro", serif;
    font-weight: 700;
    font-size: 25px;
    letter-spacing: 0.5px;
  }
  .web-address {
    fill: var(--type-white);
    font-family: "Cinzel", "Trajan Pro", serif;
    font-weight: 700;
    font-size: 18px;
    letter-spacing: 0.6px;
  }
</style>
</head>
<body>
<svg class="artboard" viewBox="0 0 1200 1000" xmlns="http://www.w3.org/2000/svg">
  <defs>
    <linearGradient id="goldSheen" x1="0" y1="0" x2="1" y2="0">
      <stop offset="0" stop-color="var(--gold-deep)"/>
      <stop offset="0.45" stop-color="var(--gold-mid)"/>
      <stop offset="0.62" stop-color="var(--gold-shine)"/>
      <stop offset="0.8" stop-color="var(--gold-mid)"/>
      <stop offset="1" stop-color="var(--gold-deep)"/>
    </linearGradient>
    <linearGradient id="flourishTone" x1="0" y1="0" x2="1" y2="1">
      <stop offset="0" stop-color="var(--flourish-light)"/>
      <stop offset="0.5" stop-color="var(--flourish-dark)"/>
      <stop offset="1" stop-color="var(--flourish-light)"/>
    </linearGradient>
    <radialGradient id="beanTone" cx="0.4" cy="0.35" r="0.7">
      <stop offset="0" stop-color="var(--bean-light)"/>
      <stop offset="1" stop-color="var(--bean-dark)"/>
    </radialGradient>
  </defs>

  <!-- size guides -->
  <g class="size-guide">
    <line x1="262" y1="290" x2="262" y2="712"/>
    <path d="M257 296 L262 290 L267 296 M257 706 L262 712 L267 706"/>
    <line x1="317" y1="757" x2="884" y2="757"/>
    <path d="M323 752 L317 757 L323 762 M878 752 L884 757 L878 762"/>
  </g>
  <text class="size-label" x="0" y="0" text-anchor="middle" transform="translate(248 501) rotate(90)">76mm</text>
  <text class="size-label" x="600" y="786" text-anchor="middle">102mm</text>

  <!-- sticker -->
  <g class="sticker">
    <rect class="label-base" x="317" y="290" width="567" height="422"/>
    <path class="flourish-field" role="img" aria-label="Grey baroque flourish pattern across the label background"
          d="M317 294 L740 362 C800 372 850 350 884 300 L884 708 L470 636 C410 626 350 650 317 700 Z"/>

    <path class="gold-band" d="M317 290 L740 356 C800 366 850 340 884 290 L884 318 C850 360 800 378 740 370 Z"/>
    <path class="gold-band" d="M884 712 L470 642 C410 632 350 660 317 712 L317 686 C350 642 410 620 470 628 Z"/>

    <text class="brand-name" x="440" y="440">VELMON</text>
    <text class="brand-name" x="490" y="489">BREW</text>

    <ellipse class="bean-photo" role="img" aria-label="Photo of a single roasted coffee bean" cx="597" cy="530" rx="46" ry="48"/>

    <rect class="blend-ribbon" x="390" y="571" width="420" height="48"/>
    <text class="blend-name" x="600" y="603" text-anchor="middle">Fairtrade Organic Blend</text>

    <text class="web-address" x="359" y="703">WWW.VELMONBREW.COM.AU</text>
  </g>
</svg>
</body>
</html>
```